KeyHarbor needs a modern business card

We are a modern conveyancing company and we need to appeal to the top (Multi-million dollar properties)and bottom on the property conveyancing market but our sweet spot is the middle of the market. I like professional with a hint of unconventional.

Target Market(s)

As above

Industry/Entity Type

Real Estate

Contact Information for Business Card

Back Of card:
thinking black with the logo and a tag line (I could be wrong about the black)
Tag line - Sound Advice, Seamless Handovers

Front of Card:
Marissa Toll (BBus (Finance) LLB)
Licensed Conveyancer
Email: marissa@keyharbor.com.au

Key Harbor
ABN: 48 913 706
Suite 14, Level 3, 9 Calloway Road Lindhurst Park, NSW 2178
Phone: 1300 682 917

Sydney - Melbourne - Brisbane (Perhaps have this along the bottom of the card)

Requirements
Must have
• Sleek, modern and top end appeal (But approachable)
Should not have
• Not too cluttered

```html
<!DOCTYPE html>
<html lang="en">
<head>
<meta charset="utf-8">
<title>KeyHarbor Business Card</title>
<link rel="stylesheet" href="https://fonts.googleapis.com/css2?family=Source+Sans+3:ital,wght@0,400;0,600;0,700;1,700&display=swap">
<style>
  :root {
    --harbor-blue: #255179;
    --harbor-blue-deep: #1f4a73;
    --card-white: #ffffff;
    --wordmark-grey: #4d4d4f;
    --backdrop: #e9e7e4;
  }
  * { margin: 0; padding: 0; box-sizing: border-box; }
  html, body {
    width: 1200px; height: 900px; overflow: hidden;
    background: var(--backdrop);
    font-family: "Source Sans 3", "Myriad Pro", sans-serif;
  }
  .canvas { position: relative; width: 1200px; height: 900px; }

  .card {
    position: absolute;
    background: var(--card-white);
    box-shadow: 0 6px 18px rgba(0,0,0,0.18);
    overflow: hidden;
  }

  /* Front of card */
  .card-front { left: 78px; top: 34px; width: 588px; height: 364px; }
  .card-front .info-band {
    position: absolute; left: 0; right: 0; top: 30px; height: 309px;
    background: var(--harbor-blue);
    color: var(--card-white);
    text-align: center;
  }
  .info-band .line { position: absolute; left: 0; right: 0; font-size: 17px; line-height: 1; }
  .info-band .holder-name { top: 21px; font-size: 23px; font-weight: 600; }
  .holder-name .credentials { font-size: 17px; font-weight: 400; }
  .holder-role { top: 47px; }
  .address-1 { top: 97px; }
  .address-2 { top: 121px; }
  .phone { top: 162px; }
  .email { top: 186px; }
  .abn { top: 231px; }
  .label { font-weight: 700; }
  .info-band .cities {
    top: 272px; font-size: 20px;
    font-weight: 700; font-style: italic;
  }
  .cities .dot { font-style: normal; font-size: 13px; margin: 0 7px; vertical-align: 3px; }

  /* Back of card */
  .card-back { left: 388px; top: 505px; width: 567px; height: 352px; background: var(--harbor-blue); }
  .card-back .brand-band {
    position: absolute; left: 0; right: 0; top: 105px; height: 158px;
    background: var(--card-white);
    text-align: center;
  }
  .brand-lockup {
    position: absolute; left: 0; right: 0; top: 50px;
    display: flex; justify-content: center; align-items: center; gap: 14px;
  }
  .brand-square { width: 34px; height: 34px; background: var(--harbor-blue); }
  .brand-name {
    font-size: 44px; font-weight: 600; color: var(--wordmark-grey);
    letter-spacing: -0.5px; line-height: 1;
  }
  .tagline {
    position: absolute; left: 0; right: 0; top: 130px;
    font-size: 17px; font-weight: 700; color: var(--harbor-blue-deep);
    line-height: 1;
  }
</style>
</head>
<body>
<main class="canvas">
  <section class="card card-front" aria-label="Front of business card">
    <div class="info-band">
      <p class="line holder-name">Marissa Toll <span class="credentials">(BBus (Finance) LLB)</span></p>
      <p class="line holder-role">Licensed Conveyancer</p>
      <p class="line address-1">Suite 14, Level 3, 9 Calloway Road</p>
      <p class="line address-2">Lindhurst Park, NSW 2178</p>
      <p class="line phone"><span class="label">Phone:</span> 1300 682 917</p>
      <p class="line email"><span class="label">Email:</span> marissa@keyharbor.com.au</p>
      <p class="line abn"><span class="label">ABN:</span> 48 913 706</p>
      <p class="line cities">Sydney<span class="dot">●</span>Melbourne<span class="dot">●</span>Brisbane</p>
    </div>
  </section>

  <section class="card card-back" aria-label="Back of business card">
    <div class="brand-band">
      <div class="brand-lockup">
        <span class="brand-square" aria-hidden="true"></span>
        <span class="brand-name">KeyHarbor</span>
      </div>
      <p class="tagline">Sound Advice, Seamless Handovers</p>
    </div>
  </section>
</main>
</body>
</html>
```